Upscale business cards needed for family business

We need professional business cards created for several family members. We are a family business holding company. We would like these relatively simple and straightforward, but also with a unique element to set them apart. Probably stick with neutral and simple colors - white, grey etc. We need space for the traditional elements, including name, title, address, email/phone number. And we will be creating several from this template so it needs to be template that is easy to switch information in and out of.

Industry/Entity Type

Business

Contact Information for Business Card

Please include the attached Dunmore Ventures logo.

Requirements
Must have
• The attached Dunmore Ventures logo.

```html
<!DOCTYPE html>
<html lang="en">
<head>
<meta charset="utf-8">
<title>Dunmore Ventures – Business Card</title>
<link href="https://fonts.googleapis.com/css2?family=Cinzel:wght@400;500&family=Montserrat:wght@400;600&display=swap" rel="stylesheet">
<style>
  :root {
    --bg: #e9e6e1;
    --ink: #1d1d1d;
    --black-top: #262626;
    --black-bottom: #050505;
    --gold: #c9a24a;
    --paper: #fbfbf9;
    --white: #ffffff;
  }
  * { box-sizing: border-box; margin: 0; padding: 0; }
  html, body { width: 1200px; height: 1022px; overflow: hidden; }
  body {
    background: var(--bg);
    display: flex;
    flex-direction: column;
    align-items: center;
    justify-content: center;
    gap: 60px;
    font-family: "Montserrat", sans-serif;
  }
  .card {
    width: 640px;
    height: 366px;
    position: relative;
    box-shadow: 0 10px 28px rgba(0,0,0,0.18);
    overflow: hidden;
  }
  .card-front {
    background: linear-gradient(160deg, var(--black-top) 0%, #111 45%, var(--black-bottom) 100%);
    display: flex;
    align-items: center;
    justify-content: center;
  }
  .brand-name {
    font-family: "Cinzel", serif;
    font-weight: 400;
    font-size: 40px;
    letter-spacing: 1px;
    color: var(--white);
  }
  .card-back {
    background: var(--paper);
    padding: 70px 0 0 96px;
    border-bottom: 5px solid var(--gold);
  }
  .person-name {
    font-family: "Cinzel", serif;
    font-weight: 500;
    font-size: 32px;
    color: var(--gold);
    line-height: 1.1;
  }
  .person-title {
    font-size: 17px;
    color: var(--ink);
    margin-top: 10px;
  }
  .address {
    font-size: 17px;
    color: var(--ink);
    line-height: 1.55;
    margin-top: 10px;
  }
  .contact-list {
    list-style: none;
    margin-top: 6px;
  }
  .contact-item {
    display: flex;
    align-items: center;
    gap: 12px;
    font-size: 17px;
    color: var(--ink);
    line-height: 1.65;
  }
  .contact-icon { width: 13px; height: 13px; flex: none; }
  .web-domain { color: var(--gold); font-weight: 600; }
</style>
</head>
<body>
  <section class="card card-front">
    <div class="brand-name">Dunmore Ventures</div>
  </section>

  <section class="card card-back">
    <h1 class="person-name">Marcus Ellery</h1>
    <p class="person-title">Director</p>
    <p class="address">Lindenweg 14/3/12<br>A - 1050, Wien</p>
    <ul class="contact-list">
      <li class="contact-item">
        <svg class="contact-icon" viewBox="0 0 16 16" aria-hidden="true"><path fill="#c9a24a" d="M3.5 1.5l2.5 2.8-1.4 1.6c.9 2 2.6 3.7 4.6 4.6l1.6-1.4 2.8 2.5-1.6 2.1C7 13.3 2.7 9 1.4 3.1z"/></svg>
        <span>+330 5128-4093</span>
      </li>
      <li class="contact-item">
        <svg class="contact-icon" viewBox="0 0 16 16" aria-hidden="true"><rect x="1.5" y="3" width="13" height="10" rx="1" fill="none" stroke="#c9a24a" stroke-width="1.6"/><path d="M2 4l6 5 6-5" fill="none" stroke="#c9a24a" stroke-width="1.6"/></svg>
        <span>info@dunmoreventures.com</span>
      </li>
      <li class="contact-item">
        <svg class="contact-icon" viewBox="0 0 16 16" aria-hidden="true"><circle cx="8" cy="8" r="6.5" fill="none" stroke="#c9a24a" stroke-width="1.5"/><ellipse cx="8" cy="8" rx="2.8" ry="6.5" fill="none" stroke="#c9a24a" stroke-width="1.2"/><path d="M1.5 8h13" stroke="#c9a24a" stroke-width="1.2"/></svg>
        <span>www.<span class="web-domain">dunmoreventures</span>.com</span>
      </li>
    </ul>
  </section>
</body>
</html>
```